Coming Soon HTML5 Animated landing page

We need a landing page showing vape movement and our logo (With some discreet movement) stating "Bold Deals on Premium E-Liquids Vaping soon" with a contemporary countdown with the colors of our logo. A Countdown will be nice (A contemporary one, Bold) providing all required files. Java Script, CSS, Graphics, Videos and of course HTML....

Target Market(s)

Male/Female 21 - 40 Years Old, Vape Lovers and E-Cigarrette consumers

Coding

Coded - Design and coding required

Number of Pages Required

2 page

Font styles to use
Sans Serif
Other font styles liked:
• Look at our logo

Colors
f37122
ffc214

Requirements
Must have
• A cool HTML5 animation, Vapor movement or exhaled. A configurable count down.
Nice to have
• Would love to see our logo forming
Should not have
• Corny and old concepts...

```html
<!DOCTYPE html>
<html lang="en">
<head>
<meta charset="utf-8">
<title>EmberMist — Coming Soon</title>
<link rel="stylesheet" href="https://fonts.googleapis.com/css2?family=Roboto+Condensed:wght@400;700&family=Montserrat:ital,wght@0,400;1,400&display=swap">
<style>
  :root {
    --ink: #000000;
    --paper: #ffffff;
    --flame: #f37122;
    --gold: #ffc214;
    --alert: #e3232c;
    --line: rgba(255,255,255,0.85);
    --panel: rgba(0,0,0,0.62);
    --hint: #bdbdbd;
  }
  * { margin: 0; padding: 0; box-sizing: border-box; }
  html, body { width: 1200px; height: 637px; overflow: hidden; background: var(--ink); }
  .page {
    position: relative; width: 1200px; height: 637px; overflow: hidden;
    color: var(--paper); font-family: "Montserrat", sans-serif;
  }
  .hero-photo {
    position: absolute; inset: 0;
    background:
      radial-gradient(ellipse 260px 320px at 470px 300px, #4a4a4a 0%, #2a2a2a 45%, transparent 80%),
      radial-gradient(ellipse 420px 260px at 300px 520px, #2e2e2e 0%, transparent 75%),
      radial-gradient(ellipse 300px 240px at 1060px 180px, #1c1c1c 0%, transparent 80%),
      #0b0b0b;
  }
  .side-panel { position: absolute; top: 0; right: 0; width: 570px; height: 637px; background: var(--panel); }

  .brand { position: absolute; left: 52px; top: 38px; }
  .brand-name {
    font-family: "Roboto Condensed", sans-serif; font-weight: 700;
    font-size: 60px; line-height: 1; color: var(--flame); letter-spacing: 1px;
  }
  .brand-tagline { margin-top: 10px; font-size: 13px; letter-spacing: 1px; color: var(--paper); }

  .launch { position: absolute; left: 52px; top: 253px; font-family: "Roboto Condensed", sans-serif; }
  .launch-title { font-size: 22px; font-weight: 400; color: var(--gold); text-transform: uppercase; white-space: nowrap; }
  .launch-title em { font-style: normal; color: var(--alert); }
  .countdown { display: flex; margin-top: 20px; }
  .countdown-unit { display: flex; flex-direction: column; }
  .countdown-value { font-weight: 700; font-size: 70px; line-height: 0.95; color: var(--alert); }
  .countdown-label { font-size: 20px; margin-top: 2px; }
  .u-days { width: 141px; } .u-hours { width: 119px; } .u-minutes { width: 123px; }

  .copyright { position: absolute; left: 52px; top: 607px; font-size: 12px; }

  .main-nav { position: absolute; left: 680px; top: 50px; display: flex; gap: 21px;
    font-family: "Roboto Condensed", sans-serif; font-size: 15px; text-transform: uppercase; }
  .main-nav a { color: var(--paper); text-decoration: none; }
  .main-nav a.is-active { color: var(--gold); }

  .contact { position: absolute; left: 680px; top: 108px; }
  .contact-title { font-family: "Roboto Condensed", sans-serif; font-weight: 700; font-size: 40px; line-height: 1; }
  .contact-list { list-style: none; margin-top: 24px; }
  .contact-list li { display: flex; align-items: center; gap: 8px; font-size: 12px; height: 30px; }
  .contact-list svg { width: 12px; height: 12px; fill: var(--gold); }
  .social { display: flex; gap: 9px; margin-top: 22px; }
  .social span { width: 29px; height: 29px; border-radius: 50%; background: var(--paper); }

  .message-form { position: absolute; left: 682px; top: 354px; width: 406px; height: 231px; border: 1px solid var(--line); }
  .field { height: 43px; border-bottom: 1px solid var(--line); padding: 0 13px;
    display: flex; align-items: center; font-size: 12px; font-style: italic; color: var(--hint); }
  .field-message { height: auto; border: 0; padding-top: 14px; align-items: flex-start; }
  .submit { position: absolute; right: -1px; bottom: -1px; width: 101px; height: 44px;
    border: 1px solid var(--line); background: transparent; color: var(--gold);
    font-family: "Roboto Condensed", sans-serif; font-size: 17px; }
</style>
</head>
<body>
<div class="page">
  <div class="hero-photo" role="img" aria-label="Dark black and white photo of a man exhaling a cloud of vapor"></div>
  <div class="side-panel"></div>

  <header class="brand">
    <div class="brand-name">EMBERMIST</div>
    <div class="brand-tagline">Bold Deals on Premium E-Liquids</div>
  </header>

  <section class="launch">
    <h2 class="launch-title">Bold Deals on Premium E-Liquids <em>Coming Soon</em></h2>
    <div class="countdown">
      <div class="countdown-unit u-days"><span class="countdown-value">157</span><span class="countdown-label">DAYS</span></div>
      <div class="countdown-unit u-hours"><span class="countdown-value">13</span><span class="countdown-label">HOURS</span></div>
      <div class="countdown-unit u-minutes"><span class="countdown-value">42</span><span class="countdown-label">MINUTES</span></div>
      <div class="countdown-unit"><span class="countdown-value">05</span><span class="countdown-label">SECONDS</span></div>
    </div>
  </section>

  <p class="copyright">Copyright © 2016-17 EmberMist.com</p>

  <nav class="main-nav">
    <a href="#">Home</a><a href="#" class="is-active">About Us</a><a href="#">Subscribe</a><a href="#">Contact Us</a>
  </nav>

  <section class="contact">
    <h1 class="contact-title">CONTACT US</h1>
    <ul class="contact-list">
      <li><svg viewBox="0 0 12 12"><path d="M6 0a4 4 0 0 0-4 4c0 3 4 8 4 8s4-5 4-8a4 4 0 0 0-4-4zm0 5.6A1.6 1.6 0 1 1 6 2.4a1.6 1.6 0 0 1 0 3.2z"/></svg>1820 NE 12th Ave Ste 310, Harbor City, 33120</li>
      <li><svg viewBox="0 0 12 12"><path d="M0 2h12v1L6 7 0 3z M0 4.3l6 4 6-4V10H0z"/></svg>hello@embermist.com</li>
      <li><svg viewBox="0 0 12 12"><path d="M2.4 0.5l2 2.2-1 1.4c.8 1.8 2.2 3.2 4 4l1.4-1 2.2 2-1.4 2.2C5 10.6 1.4 7 .5 2.3z"/></svg>1 -844-EMBERMT</li>
    </ul>
    <div class="social"><span></span><span></span><span></span><span></span></div>
  </section>

  <form class="message-form">
    <div class="field">Your Name</div>
    <div class="field">Your Email Address</div>
    <div class="field field-message">What You Want To Say...</div>
    <button type="button" class="submit">SUBMIT</button>
  </form>
</div>
</body>
</html>
```